Crestbacking Banner Ad Campaign

Overview
We require 3 different banners within the same brief, but would like you to just produce 1 banner for your initial bid.

We require a punchy message to be delivered to existing poker players. We offer the opportunity for players to play poker with our money (ie. ‘staked’), sharing the profits if they win, us taking the losses if they lose. 'Sharks' is a poker term for skilled winning players who eat up the 'fish'.. term for unskilled losing players.

The players we stake are playing no risk poker and enjoy the support of our team, as well as professional coaching free of charge. Our key messages are bulleted below, some suggestions for tag lines also. We would like some creativity input in the design/ tag lines plus of course the banners themselves delivered. See www.crestbacking-example.com for our colour scheme and shark fin logo and to get a feel for what we do.

3 different pieces of artwork required:-
2 'square', sized – 180x150
1 'normal' banner sized
Clearly we may want to resize these slightly for different uses.

Some messages we want to convey:-
• Free Bankroll $$$$
• Free Pro Coaching
• Part of a team & support network
• Risk free, stress free poker
• We are the best staking operation

Possible tag lines:-
Losing your bite?
Sharpen your teeth!
Get staked today!
Join the best, crush the rest

Thanks
Alan
Updates

Guys,

we have a strong theme with the Shark and/or our red fin logo, can you focus on that in your designs please. a Shark as per brief is a successful poker player .. a 'fish' is what they prey on..

Thanks

Alan

Industry/Entity Type

Campaign

```html
<!DOCTYPE html>
<html lang="en">
<head>
<meta charset="utf-8">
<title>Crestbacking Banner Set</title>
<link rel="stylesheet" href="https://fonts.googleapis.com/css2?family=Oswald:wght@400;500&display=swap">
<style>
  :root {
    --board-light: #2c2c2c;
    --board-dark: #121212;
    --ad-black: #07080c;
    --brand-red: #ee1a0c;
    --deep-red: #6e0a06;
    --chip-blue: #4a4f9c;
    --chip-pale: #b9b6e0;
    --text-white: #ffffff;
  }
  * { box-sizing: border-box; margin: 0; padding: 0; }
  html, body { width: 1200px; height: 960px; overflow: hidden; }
  body {
    position: relative;
    background: radial-gradient(ellipse at 50% 30%, var(--board-light) 0%, #1e1e1e 55%, var(--board-dark) 100%);
    font-family: "Oswald", "Arial Narrow", sans-serif;
    color: var(--text-white);
  }
  .brand {
    position: absolute;
    display: flex;
    align-items: center;
    gap: 8px;
    font-weight: 500;
    color: var(--text-white);
    white-space: nowrap;
  }
  .brand-dot { display: block; border-radius: 50%; background: var(--brand-red); flex: none; }

  .brand-hero { left: 0; width: 1200px; top: 120px; justify-content: center; font-size: 64px; gap: 16px; }
  .brand-hero .brand-dot { width: 40px; height: 40px; }

  .ad { position: absolute; background: var(--ad-black); overflow: hidden; }
  .ad-leader { left: 38px; width: 1120px; height: 138px; }
  .ad-leader.first { top: 295px; }
  .ad-leader.second { top: 480px; width: 1127px; }

  .scene {
    position: absolute;
    background: linear-gradient(100deg, rgba(0,0,0,0) 0%, var(--deep-red) 30%, #9c1208 55%, #1a1530 80%, rgba(0,0,0,0) 100%);
  }
  .chips {
    position: absolute;
    background: linear-gradient(90deg, var(--chip-pale), var(--chip-blue) 45%, var(--chip-pale) 55%, var(--chip-blue));
    opacity: 0.75;
  }
  .ad-leader .scene { left: 190px; top: 0; width: 560px; height: 100%; }
  .ad-leader .chips { left: 555px; top: 4px; width: 130px; height: 130px; border-radius: 6px; }
  .ad-leader.second .chips { left: 650px; }
  .ad-leader.second .scene { left: 200px; width: 820px;
    background: linear-gradient(100deg, rgba(0,0,0,0) 0%, var(--deep-red) 25%, #8e1208 45%, #241e3e 65%, rgba(20,20,40,0.6) 90%, rgba(0,0,0,0) 100%); }

  .ad-leader .brand { left: 20px; top: 62px; font-size: 26px; gap: 6px; }
  .ad-leader .brand-dot { width: 14px; height: 14px; }

  .tag { position: absolute; white-space: nowrap; line-height: 1; }
  .tag-red { color: var(--brand-red); }
  .tag-hook { font-size: 42px; font-weight: 500; }
  .tag-reply { font-size: 27px; }
  .tag-call { font-size: 54px; font-weight: 500; }
  .tag-line { font-size: 28px; }

  .ad-square { top: 686px; width: 230px; height: 192px; }
  .ad-square.offer { left: 335px; }
  .ad-square.benefits { left: 629px; }
  .ad-square .chips { left: 4px; top: 66px; width: 44px; height: 100px; border-radius: 4px; }
  .ad-square .scene { left: 0; top: 30px; width: 230px; height: 150px;
    background: radial-gradient(ellipse at 30% 50%, #2a2a5a 0%, #12122a 55%, rgba(0,0,0,0) 100%); }
  .offer-title { left: 0; width: 230px; top: 8px; text-align: center; font-size: 30px; font-weight: 500; }
  .offer .brand { left: 0; width: 230px; top: 92px; justify-content: center; font-size: 26px; gap: 6px; }
  .offer .brand-dot, .benefits .brand-dot { width: 12px; height: 12px; }
  .offer-foot { left: 0; width: 230px; top: 163px; text-align: center; font-size: 17px; }
  .benefits .brand { left: 0; width: 230px; top: 36px; justify-content: center; font-size: 19px; gap: 5px; }
  .benefits .brand-dot { width: 9px; height: 9px; }
  .benefit-list { position: absolute; left: 6px; top: 76px; list-style: none; font-size: 14.5px; line-height: 21px; }
  .benefit-list li::before { content: "\25AA"; margin-right: 5px; }
</style>
</head>
<body>

  <div class="brand brand-hero"><span class="brand-dot"></span>Crestbacking</div>

  <section class="ad ad-leader first">
    <div class="scene" role="img" aria-label="Red swoosh with playing cards and poker chips"></div>
    <div class="chips" role="img" aria-label="Stacks of poker chips"></div>
    <div class="brand"><span class="brand-dot"></span>Crestbacking</div>
    <p class="tag tag-red tag-hook" style="left:201px;top:33px;">Losing your bite?</p>
    <p class="tag tag-reply" style="left:342px;top:80px;">Sharpen your teeth!</p>
    <p class="tag tag-red tag-call" style="left:686px;top:14px;">Get staked today!</p>
    <p class="tag tag-line" style="left:686px;top:85px;">Join the best, crush the rest</p>
  </section>

  <section class="ad ad-leader second">
    <div class="scene" role="img" aria-label="Red swoosh with playing cards and poker chips"></div>
    <div class="chips" role="img" aria-label="Stacks of poker chips"></div>
    <div class="brand"><span class="brand-dot"></span>Crestbacking</div>
    <p class="tag tag-red tag-hook" style="left:244px;top:27px;">Losing your bite?</p>
    <p class="tag tag-reply" style="left:345px;top:83px;">Sharpen your teeth!</p>
    <p class="tag tag-line" style="left:701px;top:53px;">We are the best staking operation</p>
  </section>

  <section class="ad ad-square offer">
    <div class="scene" role="img" aria-label="Dark blue glow behind poker chips"></div>
    <div class="chips" role="img" aria-label="Stack of poker chips"></div>
    <p class="tag offer-title">GET STAKED TODAY!</p>
    <div class="brand"><span class="brand-dot"></span>Crestbacking</div>
    <p class="tag tag-red offer-foot">Join the best, crush the rest</p>
  </section>

  <section class="ad ad-square benefits">
    <div class="scene" role="img" aria-label="Dark blue glow behind poker chips"></div>
    <div class="brand"><span class="brand-dot"></span>Crestbacking</div>
    <ul class="benefit-list">
      <li>Free Bankroll $$$$</li>
      <li>Free Pro Coaching</li>
      <li>Part of a team &amp; support network</li>
      <li>Risk free, stress free poker</li>
      <li>We are the best staking operation</li>
    </ul>
  </section>

</body>
</html>
```